Alpforma Banner

Hi boys and girls :)

We have a little project 4u.

We need a banner in 4 sizes :

Leaderboard: 728*90
Wide SkyScraper: 160*600
Medium Rectangle: 300*250
Ribbon (special format): 990*45

Message on banner :

Either our Logo + Immigration, Integration, Naturalization

Or our Logo + Incorporation, Domicile, Secretarial Services

And if space allows for it www.alpforma-example.com as well.

We are looking for a clean design, check our Website for inspiration concerning colors.

```html
<!DOCTYPE html>
<html lang="en">
<head>
<meta charset="utf-8">
<title>Alpforma Banner Set</title>
<link rel="stylesheet" href="https://fonts.googleapis.com/css2?family=Marcellus&display=swap">
<style>
  :root {
    --stage-light: #ececec;
    --stage-dark: #cdcdcd;
    --brand-red: #b50d12;
    --text-red: #9e1a1f;
    --band-red: #d90d0d;
    --band-deep: #a80808;
    --band-orange: #ff6a00;
    --panel-white: #ffffff;
    --panel-grey: #e4e4e4;
  }
  html, body {
    margin: 0;
    padding: 0;
    width: 1200px;
    height: 1000px;
    overflow: hidden;
  }
  body {
    position: relative;
    background: radial-gradient(ellipse at 50% 55%, var(--stage-light) 0%, var(--stage-dark) 100%);
    font-family: "Marcellus", "Times New Roman", serif;
  }
  .banner {
    position: absolute;
    overflow: hidden;
    box-shadow: 0 2px 6px rgba(0,0,0,0.25);
  }
  .accent-band {
    position: absolute;
    left: 0;
    width: 100%;
    background: linear-gradient(90deg, var(--band-red) 0%, var(--band-deep) 55%, var(--band-orange) 100%);
  }
  .accent-band.top { top: 0; }
  .accent-band.bottom { bottom: 0; }
  .brand-name {
    position: absolute;
    color: var(--brand-red);
    font-family: "Marcellus", "Times New Roman", serif;
    font-weight: 400;
    white-space: nowrap;
    margin: 0;
    line-height: 1;
  }
  .tagline {
    position: absolute;
    color: var(--text-red);
    text-transform: uppercase;
    margin: 0;
    white-space: nowrap;
  }

  /* Leaderboard */
  .leaderboard {
    left: 80px; top: 28px; width: 1073px; height: 131px;
    background: radial-gradient(ellipse at 68% 40%, var(--panel-white) 30%, var(--panel-grey) 100%);
  }
  .leaderboard .accent-band { height: 18px; }
  .leaderboard .tagline { left: 31px; top: 42px; font-size: 16px; letter-spacing: 0.06em; }
  .leaderboard .brand-name { left: 634px; top: 52px; font-size: 42px; }

  /* Wide skyscraper */
  .skyscraper {
    left: 256px; top: 208px; width: 192px; height: 720px;
    background: radial-gradient(ellipse at 50% 45%, var(--panel-white) 45%, var(--panel-grey) 100%);
  }
  .skyscraper .accent-band.top { height: 14px; }
  .skyscraper .accent-band.bottom { height: 70px; }
  .skyscraper .brand-name { left: 0; width: 100%; text-align: center; top: 292px; font-size: 36px; }
  .skyscraper .tagline {
    left: 0; width: 100%; top: 516px; text-align: center;
    font-size: 12.5px; line-height: 21.5px; letter-spacing: 0.02em;
  }

  /* Medium rectangle */
  .rectangle {
    left: 542px; top: 213px; width: 403px; height: 335px;
    background: radial-gradient(ellipse at 50% 45%, var(--panel-white) 40%, var(--panel-grey) 100%);
  }
  .rectangle .accent-band.top { height: 10px; }
  .rectangle .accent-band.bottom { height: 36px; }
  .rectangle .brand-name { left: 0; width: 100%; text-align: center; top: 128px; font-size: 72px; }

  /* Ribbon badge */
  .ribbon-badge {
    position: absolute;
    left: 597px; top: 730px; width: 186px; height: 58px;
    display: flex; align-items: center; justify-content: center; gap: 8px;
  }
  .ribbon-badge .dot {
    width: 14px; height: 14px; border-radius: 50%;
    background: var(--brand-red);
  }
  .ribbon-badge .brand-name { position: static; font-size: 30px; }
</style>
</head>
<body>

  <section class="banner leaderboard">
    <div class="accent-band bottom" role="img" aria-label="Decorative red, yellow and orange swoosh band"></div>
    <p class="tagline">Immigration, Integration, Naturalization</p>
    <p class="brand-name">Alpforma</p>
  </section>

  <section class="banner skyscraper">
    <div class="accent-band top" role="img" aria-label="Decorative red swoosh band"></div>
    <div class="accent-band bottom" role="img" aria-label="Decorative red, yellow and orange swoosh band"></div>
    <p class="brand-name">Alpforma</p>
    <p class="tagline">Immigration<br>Integration<br>Naturalization</p>
  </section>

  <section class="banner rectangle">
    <div class="accent-band top" role="img" aria-label="Decorative red swoosh band"></div>
    <div class="accent-band bottom" role="img" aria-label="Decorative red, yellow and orange swoosh band"></div>
    <p class="brand-name">Alpforma</p>
  </section>

  <div class="ribbon-badge">
    <span class="dot"></span>
    <p class="brand-name">Alpforma</p>
  </div>

</body>
</html>
```